New Lead input page design

Attached is our concept of a new lead input screen for the back-end of our website which is a tool for a loan agent (2 page PDF attached)

1. This is the first of many other data input screen projects for our website, so the designer that ends up with us will have quite a bit of add on new projects.

2. HERE IS THE LINK WITH THE SAMPLE OF ALL THE CURRENT CONTROLS:
http://apps.brimtally.com/controlWidgets.html

3. The colors and hues of: either GREEN & GREYS or BLUE & GREYS.

4. I think some gradients and shadows adds depth and sophistication. Basically trying to get away from old school flat, one dimensional data screen inputs and add some design flare to it.

5. Upon completion we will need the HTML of the design etc and we will code the input fields directly.

6. See attached files for the entire input screen. Please also add the data input space (see sample) to your design.

Thank you

Reason: We are extending the deadline to give us time to ask current designs to complete slight revisions

Reason: Finalizing the selection for one last variation detailed to current designers

```html
<!DOCTYPE html>
<html lang="en">
<head>
<meta charset="utf-8">
<title>New Lead Input</title>
<link rel="stylesheet" href="https://fonts.googleapis.com/css2?family=Questrial&family=Arimo:wght@400&display=swap">
<style>
  :root {
    --canvas-bg: #a5a5a5;
    --panel-bg: #5a5a5a;
    --panel-border: #ffffff;
    --header-green: #8aa800;
    --field-bg: #ffffff;
    --field-text: #7a7a7a;
    --label-text: #ffffff;
    --button-top: #9cc000;
    --button-bottom: #5a7600;
    --button-text: #111111;
  }
  html, body {
    margin: 0;
    padding: 0;
    width: 1200px;
    height: 842px;
    overflow: hidden;
    background: var(--canvas-bg);
  }
  .canvas {
    position: relative;
    width: 1200px;
    height: 842px;
    font-family: "Arimo", Arial, sans-serif;
  }
  .lead-form {
    position: absolute;
    left: 317px;
    top: 105px;
    width: 548px;
    height: 624px;
    background: var(--panel-bg);
    border: 2px solid var(--panel-border);
    border-radius: 14px;
    overflow: hidden;
  }
  .lead-form__header {
    height: 76px;
    background: var(--header-green);
    display: flex;
    align-items: center;
    justify-content: center;
  }
  .lead-form__title {
    margin: 0;
    font-family: "Questrial", "Century Gothic", sans-serif;
    font-weight: 400;
    font-size: 44px;
    letter-spacing: 1px;
    color: #ffffff;
  }
  .field-row {
    position: absolute;
    left: 0;
    width: 100%;
    height: 44px;
  }
  .field-row__label {
    position: absolute;
    right: 396px;
    top: 16px;
    font-size: 17px;
    color: var(--label-text);
    white-space: nowrap;
  }
  .field-row__input {
    position: absolute;
    left: 168px;
    top: 0;
    width: 317px;
    height: 44px;
    padding-left: 20px;
    box-sizing: content-box;
    background: var(--field-bg);
    border-radius: 18px;
    font-size: 14px;
    line-height: 44px;
    color: var(--field-text);
  }
  .field-row__input--large { font-size: 16px; line-height: 40px; }
  .field-row__input--low { line-height: 54px; }
  .submit-button {
    position: absolute;
    left: 368px;
    top: 540px;
    width: 130px;
    height: 40px;
    border: 2px solid #ffffff;
    border-radius: 22px;
    background: linear-gradient(to bottom, var(--button-top) 0%, #86a800 45%, var(--button-bottom) 100%);
    box-shadow: 1px 3px 4px rgba(0,0,0,0.45);
    color: var(--button-text);
    font-family: "Arimo", Arial, sans-serif;
    font-size: 20px;
    text-align: center;
    line-height: 42px;
  }
</style>
</head>
<body>
<main class="canvas">
  <section class="lead-form">
    <header class="lead-form__header">
      <h1 class="lead-form__title">New Lead Input</h1>
    </header>

    <div class="field-row" style="top:141px">
      <span class="field-row__label">Last Name*</span>
      <div class="field-row__input">Polo</div>
    </div>
    <div class="field-row" style="top:223px">
      <span class="field-row__label">Email*</span>
      <div class="field-row__input">Email Address</div>
    </div>
    <div class="field-row" style="top:305px">
      <span class="field-row__label">Phone Number*</span>
      <div class="field-row__input">Phone Number</div>
    </div>
    <div class="field-row" style="top:387px">
      <span class="field-row__label">City*</span>
      <div class="field-row__input field-row__input--large">Costa Mesa</div>
    </div>
    <div class="field-row" style="top:469px">
      <span class="field-row__label" style="top:21px">State*</span>
      <div class="field-row__input field-row__input--low">CA</div>
    </div>

    <div class="submit-button">SUBMIT</div>
  </section>
</main>
</body>
</html>
```